Pine Ridge Traders, LLC- Global Beverage Company with 100% Cold Chain Logistics

Hey All, My Name is Tom, I am a young business owner in a competitive export space, but my niche is that I am shipping all of my beer around the world, "100% Cold Chain". This model is more costly, but it protects the integrity of the beer itself and will give folks in foreign countries the best representation of what US Craft Beer has to offer.

I am not a branding guy and don't claim to be one, I am a salesperson first, and will be referring to all of you to create something great that will be memorable.

I am looking for a basic Business Card Design for my Craft Beer Export company. I sell US Craft Beer in several countries around the globe. Austrailia, China, Taiwan, Chile, France, New Zealand... to name a few.

I am looking for a sleek, modern, and fresh design. Quickly!

Thanks for your consideration!

Cheers,

Tom

Target Market(s)

International

Contact Information for Business Card

Tom Reilly
Founder- World Brew Guy
Tom@PineRidgeTraders.example
@WorldBrewGuy- Instagram only
www.Pineridgetraders.example
@PineRidgeTradersAU- Instagram Only

Font styles to use
Serif

Colors
0592cd
ffffff

Requirements
Must have
• Name-
• Title-
• Email-
• Social Media Handle-
• Company Website-
Nice to have
• Nice Logo/ Images on Card
Should not have
• Tacky Beer Images

```html
<!DOCTYPE html>
<html lang="en">
<head>
<meta charset="utf-8">
<title>Pine Ridge Traders – Business Card</title>
<link rel="stylesheet" href="https://fonts.googleapis.com/css2?family=Montserrat:ital,wght@0,300;0,400;0,600;1,900&display=swap">
<style>
  :root {
    --brand-sky: #0592cd;
    --brand-blue: #1a6fb8;
    --brand-indigo: #2e3192;
    --ink: #3a3a3a;
    --paper: #ffffff;
    --canvas: #ffffff;
  }
  * { box-sizing: border-box; margin: 0; padding: 0; }
  html, body {
    width: 1200px; height: 1200px; overflow: hidden;
    background: var(--canvas);
    font-family: "Montserrat", sans-serif;
  }
  .canvas { position: relative; width: 1200px; height: 1200px; }

  .card {
    position: absolute;
    left: 251px;
    width: 704px;
    overflow: hidden;
  }
  .card--front { top: 98px; height: 459px; }
  .card--back {
    top: 604px; height: 453px;
    background: var(--paper);
    border: 1px solid #e6e8ee;
  }

  .front-bg { position: absolute; inset: 0; width: 100%; height: 100%; }

  .front-wordmark {
    position: absolute; inset: 0;
    display: flex; align-items: center; justify-content: center;
    color: var(--paper);
    font-weight: 600;
    font-size: 30px;
    letter-spacing: 0.04em;
  }

  .identity {
    position: absolute;
    left: 285px; top: 74px;
  }
  .identity__name {
    font-weight: 900; font-style: italic;
    font-size: 48px; line-height: 1;
    letter-spacing: -0.02em;
    background: linear-gradient(90deg, var(--brand-sky), var(--brand-indigo));
    -webkit-background-clip: text; background-clip: text;
    color: transparent;
    white-space: nowrap;
  }
  .identity__title {
    margin-top: 12px;
    font-weight: 300; font-size: 18.5px;
    letter-spacing: 0.06em;
    color: var(--ink);
    white-space: nowrap;
  }
  .identity__dot {
    display: inline-block; width: 8px; height: 8px;
    border-radius: 50%; background: var(--brand-sky);
    margin: 0 10px; vertical-align: middle; position: relative; top: -2px;
  }

  .contacts {
    position: absolute; left: 79px; top: 247px;
    list-style: none;
  }
  .contacts__item {
    display: flex; align-items: center;
    height: 52px;
    font-weight: 300; font-size: 19px;
    letter-spacing: 0.03em; color: var(--ink);
  }
  .contacts__icon { width: 38px; height: 38px; margin-right: 24px; flex: none; }
</style>
</head>
<body>
<main class="canvas">

  <section class="card card--front" aria-label="Card front">
    <svg class="front-bg" viewBox="0 0 704 459" preserveAspectRatio="none" aria-hidden="true">
      <defs>
        <linearGradient id="frontBase" x1="0" y1="1" x2="1" y2="0">
          <stop offset="0" stop-color="#2e3192"/>
          <stop offset="0.45" stop-color="#1f64b4"/>
          <stop offset="1" stop-color="#0592cd"/>
        </linearGradient>
        <linearGradient id="frontSweep" x1="0" y1="1" x2="1" y2="0">
          <stop offset="0" stop-color="#0592cd" stop-opacity="0.8"/>
          <stop offset="0.5" stop-color="#1a6fb8" stop-opacity="0.5"/>
          <stop offset="1" stop-color="#0592cd" stop-opacity="0.9"/>
        </linearGradient>
      </defs>
      <rect width="704" height="459" fill="url(#frontBase)"/>
      <path d="M0 352 C 150 150, 330 40, 455 0 L 704 0 L 704 110 C 600 250, 480 400, 250 459 L 0 459 Z" fill="url(#frontSweep)" opacity="0.55"/>
      <path d="M0 352 C 150 150, 330 40, 455 0" stroke="#2a9ad6" stroke-width="2" fill="none" opacity="0.5"/>
    </svg>
    <div class="front-wordmark">Pine Ridge Traders</div>
  </section>

  <section class="card card--back" aria-label="Card back">
    <div class="identity">
      <h1 class="identity__name">Tom Reilly</h1>
      <p class="identity__title">WORLD BREW GUY<span class="identity__dot"></span>FOUNDER</p>
    </div>

    <ul class="contacts">
      <li class="contacts__item">
        <svg class="contacts__icon" viewBox="0 0 38 38" aria-hidden="true">
          <rect x="3" y="3" width="32" height="32" rx="7" fill="none" stroke="var(--brand-indigo)" stroke-width="3"/>
        </svg>
        @WorldBrewGuy
      </li>
      <li class="contacts__item">
        <svg class="contacts__icon" viewBox="0 0 38 38" aria-hidden="true">
          <rect x="2" y="5" width="34" height="28" rx="6" fill="none" stroke="var(--brand-blue)" stroke-width="3"/>
          <path d="M9 14 L19 22 L29 14" fill="none" stroke="var(--brand-indigo)" stroke-width="3" stroke-linecap="round" stroke-linejoin="round"/>
        </svg>
        tom@pineridgetraders.example
      </li>
      <li class="contacts__item">
        <svg class="contacts__icon" viewBox="0 0 38 38" aria-hidden="true">
          <g fill="none" stroke="var(--brand-blue)" stroke-width="2.6">
            <circle cx="19" cy="19" r="16"/>
            <ellipse cx="19" cy="19" rx="7" ry="16"/>
            <line x1="3" y1="19" x2="35" y2="19"/>
            <path d="M6 11 H32 M6 27 H32"/>
          </g>
        </svg>
        www.pineridgetraders.example
      </li>
    </ul>
  </section>

</main>
</body>
</html>
```